Need a new design for Glass Cleaner label. The brand name already exists i.e. BRIXO. Pell is the company name. Looking for new design. It's application is for cleaning glasses in houses, cars, offices e.t.c. Our product gives streak free shine and anti static effect. Images of old label design is attached. Bottle will be same as before. It's better to show a car as well in the design but not necessary. New logo's of brixo can also be designed.

Target Market(s)

Household and automobile

Industry/Entity Type

It Company

```html
<!DOCTYPE html>
<html lang="en">
<head>
<meta charset="utf-8">
<title>BRIXO Glass Cleaner Label</title>
<link rel="stylesheet" href="https://fonts.googleapis.com/css2?family=Fira+Sans+Condensed:wght@400;500;700;800;900&display=swap">
<style>
  :root {
    --page-bg: #ececec;
    --brand-red: #d4102a;
    --deep-red: #b00b22;
    --sky-light: #e9f3fb;
    --sky-mid: #6fa3dc;
    --label-blue: #3f6fc0;
    --label-navy: #283f8e;
    --tagline-blue: #3b6fb4;
    --tick-navy: #1d3c8a;
    --white: #ffffff;
  }
  * { margin: 0; padding: 0; box-sizing: border-box; }
  html, body { width: 1200px; height: 1194px; overflow: hidden; background: var(--page-bg); }
  .canvas {
    position: relative;
    width: 1200px;
    height: 1194px;
    font-family: "Fira Sans Condensed", sans-serif;
  }
  .label-shape { position: absolute; inset: 0; }
  .company-name {
    position: absolute;
    left: 598px; top: 206px;
    font-size: 96px; font-weight: 800;
    color: var(--brand-red);
    line-height: 1;
  }
  .tagline {
    position: absolute;
    left: 398px; top: 298px;
    width: 140px;
    text-align: center;
    font-size: 25px; font-weight: 700;
    line-height: 1.05;
    color: var(--tagline-blue);
    transform: rotate(-6deg);
  }
  .tagline .tagline-strong { letter-spacing: 2px; font-size: 27px; }
  .product-name {
    position: absolute;
    left: 338px; top: 410px;
    width: 460px;
    text-align: center;
    font-size: 186px; font-weight: 900;
    letter-spacing: -5px;
    line-height: 1;
    color: var(--brand-red);
    transform: rotate(-3deg);
    white-space: nowrap;
  }
  .action-title {
    position: absolute;
    left: 352px; top: 668px;
    font-size: 37px; font-weight: 500;
    color: var(--white);
    line-height: 1;
    white-space: nowrap;
  }
  .action-list {
    position: absolute;
    left: 350px; top: 712px;
    font-size: 12px; font-weight: 500;
    color: var(--deep-red);
    white-space: nowrap;
    line-height: 1;
  }
  .action-list .tick { color: var(--tick-navy); font-weight: 800; }
  .category {
    position: absolute;
    left: 355px; top: 742px;
    font-size: 60px; font-weight: 500;
    color: var(--white);
    line-height: 1;
  }
  .volume {
    position: absolute;
    left: 355px; top: 970px;
    font-size: 28px; font-weight: 500;
    color: var(--white);
    line-height: 1;
  }
  .usage-note {
    position: absolute;
    left: 580px; top: 944px;
    width: 300px;
    text-align: center;
    font-size: 16px; font-weight: 700;
    line-height: 1.3;
    color: var(--white);
    white-space: nowrap;
  }
</style>
</head>
<body>
<div class="canvas">
  <svg class="label-shape" width="1200" height="1194" viewBox="0 0 1200 1194">
    <defs>
      <linearGradient id="labelFill" x1="0" y1="0" x2="0" y2="1">
        <stop offset="0" stop-color="var(--sky-mid)"/>
        <stop offset="0.12" stop-color="var(--sky-light)"/>
        <stop offset="0.3" stop-color="var(--white)"/>
        <stop offset="0.5" stop-color="var(--sky-mid)"/>
        <stop offset="0.75" stop-color="var(--label-blue)"/>
        <stop offset="1" stop-color="var(--label-navy)"/>
      </linearGradient>
      <linearGradient id="bandFill" x1="0" y1="0" x2="1" y2="0">
        <stop offset="0" stop-color="var(--brand-red)"/>
        <stop offset="0.55" stop-color="var(--deep-red)"/>
        <stop offset="1" stop-color="var(--brand-red)"/>
      </linearGradient>
      <linearGradient id="windowFill" x1="0" y1="0" x2="0" y2="1">
        <stop offset="0" stop-color="#dfe9f3"/>
        <stop offset="0.4" stop-color="#4f8fd4"/>
        <stop offset="1" stop-color="#a9c8e8"/>
      </linearGradient>
      <clipPath id="labelClip">
        <path d="M320 330 Q320 300 350 288 L660 144 Q678 137 700 137 L780 137 Q798 137 802 156 L890 690 L890 1080 Q890 1098 870 1100 L390 1142 Q330 1146 322 1100 Z"/>
      </clipPath>
    </defs>
    <g clip-path="url(#labelClip)">
      <rect x="300" y="120" width="620" height="1040" fill="url(#labelFill)"/>
      <rect x="300" y="740" width="620" height="67" fill="url(#bandFill)"/>
    </g>
    <rect x="560" y="614" width="314" height="300" fill="url(#windowFill)" stroke="var(--white)" stroke-width="8"
          role="img" aria-label="Open white-framed window showing blue sky with clouds"/>

    <g class="use-icons" fill="var(--white)">
      <circle cx="374" cy="853" r="27" fill="var(--brand-red)" stroke="var(--white)" stroke-width="3"/>
      <path d="M358 853 L374 838 L390 853 L386 853 L386 867 L362 867 L362 853 Z"/>
      <circle cx="415" cy="904" r="27" fill="var(--brand-red)" stroke="var(--white)" stroke-width="3"/>
      <rect x="401" y="900" width="28" height="4"/>
      <rect x="418" y="904" width="9" height="14"/>
      <rect x="403" y="904" width="3" height="14"/>
      <rect x="404" y="888" width="4" height="12"/>
      <circle cx="473" cy="939" r="27" fill="var(--brand-red)" stroke="var(--white)" stroke-width="3"/>
      <path d="M455 933 L491 933 L489 944 Q488 948 483 948 L478 948 Q475 948 474 943 L472 940 L470 943 Q469 948 466 948 L461 948 Q456 948 455 944 Z"/>
      <circle cx="534" cy="972" r="27" fill="var(--brand-red)" stroke="var(--white)" stroke-width="3"/>
      <path d="M518 977 L518 969 L524 961 L544 961 L550 969 L550 977 Z"/>
      <circle cx="524" cy="978" r="3.5"/>
      <circle cx="544" cy="978" r="3.5"/>
    </g>
  </svg>

  <div class="company-name">Pell</div>
  <div class="tagline">Outstanding<br><span class="tagline-strong">STREAK</span><br>FREE Shine</div>
  <div class="product-name">BRIXO</div>
  <div class="action-title">triple action</div>
  <div class="action-list"><span class="tick">✓</span>anti-static<span class="tick">✓</span>anti-dust<span class="tick">✓</span>anti-streak</div>
  <div class="category">Glass</div>
  <div class="volume">500ml</div>
  <div class="usage-note">Suitable for<br>home, office, car and all glass surfaces.</div>
</div>
</body>
</html>
```